Vinyl Banner for bike shop to hang outside a railway station and attract new customers)

We run a small indenendent bike shop on the main campus at Harwell Vale University.

Just up the road from us is the Marlowe Park station where thousands of commuters enter and exit each day.

We have permssion to hang a vinyl banner 1.2m x 3.5m directly opposite the ttrain station entrance/exit.

Vinyl Banner adverts must:
Clearly display Fennick Wheels logo
Include directional arrows pointing left.
List our email, url and phone details
Promote the purchasing of new bikes through Pedalpath
Promote Bike Hire
Promote repairs and servicing of all bikes.
Promote sales of accesories including and especially Brackenlok D locks
Be friendly to a female target audience without excluding men.
Be in keeping with our logo font etc.
Be a significant impovemnet on our current banner
Include logo's of our major brands (Tolver Bikes, Hollowmere Bikes, Quell Bikes, Vosk Bikes, Pellam Bikes, Zantry Bikes)

Include "10% OFF for all PCW Staff'

I've added some image files you may or may not wish to use. All of which are currently used somewhere on our website.

Target Market(s)

Commuters, Students,

Industry/Entity Type

Shop

Requirements
Must have
• Our logo and brand logo's
Nice to have
• We generally use Exo font
Should not have
• Clip art!!!!

```html
<!DOCTYPE html>
<html lang="en">
<head>
<meta charset="utf-8">
<title>Fennick Wheels – Station Banner</title>
<link href="https://fonts.googleapis.com/css2?family=Exo+2:wght@400;500;700&display=swap" rel="stylesheet">
<style>
  :root {
    --page: #000000;
    --banner-dark: #1c1c1c;
    --banner-mid: #3a3a3a;
    --photo-light: #e9e6e0;
    --photo-warm: #b9ada0;
    --photo-shade: #5a5550;
    --text-white: #ffffff;
    --headline-tint: #eaf6fb;
    --accent-cyan: #3fd6e0;
    --accent-cyan-deep: #1fb3c4;
    --offer-red: #d8101a;
    --strip-white: #ffffff;
    --strip-text: #1a1a1a;
    --logo-fill: #1e1e1e;
  }
  * { box-sizing: border-box; margin: 0; padding: 0; }
  html, body {
    width: 1200px; height: 1000px; overflow: hidden;
    background: var(--page);
    font-family: "Exo 2", sans-serif;
  }
  .canvas { position: relative; width: 1200px; height: 1000px; }

  .banner {
    position: absolute; left: 17px; top: 321px;
    width: 1162px; height: 399px;
    border: 1px solid #d8d8d8;
    overflow: hidden;
    background: linear-gradient(180deg, var(--banner-dark) 0%, var(--banner-mid) 55%, #2a2a2a 100%);
  }
  .banner__skyline {
    position: absolute; right: 0; bottom: 0; width: 640px; height: 210px;
    background: linear-gradient(180deg, rgba(80,80,80,0) 0%, rgba(95,92,88,.55) 45%, rgba(60,58,55,.85) 100%);
  }
  .banner__photo {
    position: absolute; left: 0; top: 0; width: 560px; height: 100%;
    background:
      radial-gradient(ellipse 260px 220px at 180px 230px, var(--photo-light) 0%, rgba(233,230,224,.4) 55%, rgba(233,230,224,0) 100%),
      linear-gradient(90deg, var(--photo-warm) 0%, var(--photo-shade) 60%, rgba(40,40,40,0) 100%);
  }

  .brand-mark {
    position: absolute; left: 14px; top: 12px;
    width: 111px; height: 111px; border-radius: 50%;
    background: var(--logo-fill);
    border: 3px solid var(--text-white);
    display: flex; flex-direction: column; align-items: center; justify-content: center;
    color: var(--text-white); font-weight: 500; font-size: 19px; line-height: 1.05;
    text-align: center; letter-spacing: .5px;
  }

  .offer-badge {
    position: absolute; left: 1030px; top: 48px; width: 110px; height: 110px;
  }
  .offer-badge__text {
    position: absolute; inset: 0;
    display: flex; flex-direction: column; align-items: center; justify-content: center;
    color: var(--text-white); text-align: center; line-height: 1.1;
  }
  .offer-badge__pct { font-size: 25px; font-weight: 500; }
  .offer-badge__line { font-size: 13px; }

  .pointer { position: absolute; left: 425px; top: 165px; width: 96px; height: 68px; }

  .headline {
    position: absolute; left: 527px; top: 110px;
    color: var(--headline-tint); font-weight: 400;
    text-shadow: 0 2px 6px rgba(0,0,0,.5);
  }
  .headline__main { display: block; font-size: 76px; line-height: 80px; }
  .headline__sub { display: block; font-size: 47px; line-height: 48px; margin-left: 8px; color: var(--text-white); }

  .services {
    position: absolute; left: 531px; top: 244px;
    color: var(--text-white); font-weight: 700; font-size: 21px; letter-spacing: .6px;
    white-space: nowrap;
  }
  .contact {
    position: absolute; left: 529px; top: 275px;
    display: flex; gap: 16px; color: var(--text-white); font-size: 14px; white-space: nowrap;
  }
  .contact__item { display: flex; align-items: center; gap: 5px; }
  .contact__icon {
    width: 13px; height: 13px; border-radius: 2px; background: var(--accent-cyan-deep);
    display: flex; align-items: center; justify-content: center;
  }

  .brand-strip {
    position: absolute; left: 559px; top: 351px; width: 520px; height: 31px;
    background: var(--strip-white);
    display: flex; align-items: center; justify-content: space-evenly;
    color: var(--strip-text); font-weight: 700; font-size: 14px; letter-spacing: .3px;
  }
</style>
</head>
<body>
<div class="canvas">
  <section class="banner">
    <div class="banner__skyline" role="img" aria-label="City skyline with tall towers at dusk"></div>
    <div class="banner__photo" role="img" aria-label="Commuter in a checked shirt riding a road bike beside the river in sunlight"></div>

    <div class="brand-mark"><span>FENNICK</span><span>WHEELS</span></div>

    <div class="offer-badge">
      <svg width="110" height="110" viewBox="0 0 110 110" aria-hidden="true">
        <polygon fill="var(--offer-red)" points="110,55 101.1,64.2 105.8,76.1 94.1,81.1 93.9,93.9 81.1,94.1 76.1,105.8 64.2,101.1 55,110 45.8,101.1 33.9,105.8 28.9,94.1 16.1,93.9 15.9,81.1 4.2,76.1 8.9,64.2 0,55 8.9,45.8 4.2,33.9 15.9,28.9 16.1,16.1 28.9,15.9 33.9,4.2 45.8,8.9 55,0 64.2,8.9 76.1,4.2 81.1,15.9 93.9,16.1 94.1,28.9 105.8,33.9 101.1,45.8"/>
      </svg>
      <div class="offer-badge__text">
        <span class="offer-badge__pct">10%</span>
        <span class="offer-badge__line">OFF for all</span>
        <span class="offer-badge__line">PCW Staff</span>
      </div>
    </div>

    <svg class="pointer" viewBox="0 0 96 68" aria-hidden="true">
      <defs>
        <linearGradient id="arrowFill" x1="0" y1="0" x2="0" y2="1">
          <stop offset="0" stop-color="#7fe9f0"/>
          <stop offset="1" stop-color="var(--accent-cyan-deep)"/>
        </linearGradient>
      </defs>
      <polygon fill="url(#arrowFill)" points="0,34 40,0 40,18 96,18 96,50 40,50 40,68"/>
    </svg>

    <h1 class="headline">
      <span class="headline__main">Here’s The Bike</span>
      <span class="headline__sub">You’ve Always Wanted</span>
    </h1>

    <p class="services">PURCHASE | HIRE | REPAIR | SERVICE | ACCESSORIES</p>

    <div class="contact">
      <span class="contact__item">
        <span class="contact__icon"><svg width="9" height="9" viewBox="0 0 10 10"><path d="M2 1 L4 1 L4.6 3.2 L3.4 4 Q4.4 6 6 6.6 L6.8 5.4 L9 6 L9 8 Q8.5 9 7.5 9 Q2 8 1 2.5 Q1 1.5 2 1Z" fill="#fff"/></svg></span>
        0800 555 0142
      </span>
      <span class="contact__item">
        <span class="contact__icon" style="border-radius:50%"><svg width="9" height="9" viewBox="0 0 10 10"><circle cx="5" cy="5" r="4" fill="none" stroke="#fff"/><path d="M1 5H9M5 1V9" stroke="#fff"/></svg></span>
        www.fennickwheels.org.uk
      </span>
      <span class="contact__item">
        <span class="contact__icon"><svg width="9" height="9" viewBox="0 0 10 10"><circle cx="5" cy="5" r="2" fill="none" stroke="#fff"/><path d="M7 3V6Q7 7.5 8.5 7M8.5 5A3.5 3.5 0 1 0 6.5 8.2" fill="none" stroke="#fff"/></svg></span>
        Email: info@fennickwheels.org.uk
      </span>
    </div>

    <div class="brand-strip">
      <span>TOLVER</span>
      <span>HOLLOWMERE</span>
      <span>BRACKENLOK</span>
      <span>KORVANE</span>
      <span>QUELL</span>
    </div>
  </section>
</div>
</body>
</html>
```